Electrical panel service sticker w Bucket truck & Logo

We have a rather plain sticker we put on lighting panels to remind customers who to call for service. We want to redesign them with brushed aluminum background. We want a remake of the sticker with the outline of a bucket truck. You'll need to find or draw the outling of a bucket truck maybe with the boom up slightly as we will get these stickers die cut.

We want LOGO with Ph.# and Email.
Electrical * Lighting * Sign Service

Target Market(s)

Commercial property managers

Industry/Entity Type

Property Management

Requirements
Must have
• Bucket Truck Outline

```html
<!DOCTYPE html>
<html lang="en">
<head>
<meta charset="utf-8">
<title>Brightline Upkeep – Panel Service Sticker</title>
<link rel="stylesheet" href="https://fonts.googleapis.com/css2?family=Oswald:wght@500;700&family=Montserrat:wght@600;800&family=Open+Sans:wght@400&display=swap">
<style>
  :root {
    --stage: #3f3f3f;
    --stage-edge: #353535;
    --alu-light: #d4d7da;
    --alu-mid: #bfc3c6;
    --alu-dark: #a9adb1;
    --brand-red: #ec1c24;
    --brand-blue: #26368c;
    --ink: #141414;
    --truck: #0c0c0c;
  }
  * { margin: 0; padding: 0; box-sizing: border-box; }
  html, body { width: 1200px; height: 1200px; overflow: hidden; }
  body {
    background: radial-gradient(circle at 50% 45%, #4a4a4a 0%, var(--stage) 55%, var(--stage-edge) 100%);
    position: relative;
  }
  .sticker {
    position: absolute;
    left: 179px; top: 272px;
    width: 842px; height: 748px;
    background:
      repeating-linear-gradient(180deg, rgba(255,255,255,.18) 0 1px, rgba(0,0,0,.05) 1px 2px, rgba(255,255,255,0) 2px 4px),
      linear-gradient(90deg, var(--alu-mid) 0%, var(--alu-light) 30%, var(--alu-dark) 55%, var(--alu-light) 80%, var(--alu-mid) 100%);
  }
  .truck-art {
    position: absolute;
    left: 443px; top: 202px;
    width: 305px; height: 253px;
    border-radius: 10px;
    background: linear-gradient(180deg, #2a2a2a 0%, var(--truck) 100%);
  }
  .line {
    position: absolute;
    left: 0; width: 1200px;
    text-align: center;
    white-space: nowrap;
    line-height: 1;
  }
  .brand-name {
    font-family: "Oswald", sans-serif;
    font-weight: 700;
    color: var(--brand-red);
    text-transform: uppercase;
  }
  .brand-name.first { top: 460px; font-size: 96px; letter-spacing: 1px; }
  .brand-name.second { top: 579px; font-size: 106px; letter-spacing: 6px; }
  .brand-suffix {
    top: 685px;
    font-family: "Open Sans", sans-serif;
    font-weight: 400;
    font-size: 30px;
    letter-spacing: 1px;
    color: var(--brand-blue);
    text-transform: uppercase;
  }
  .service-call {
    top: 719px;
    font-family: "Oswald", sans-serif;
    font-weight: 500;
    font-size: 84px;
    color: var(--ink);
    transform: scaleX(0.8);
    transform-origin: 600px 0;
  }
  .phone {
    top: 804px;
    font-family: "Montserrat", sans-serif;
    font-weight: 800;
    font-size: 98px;
    color: var(--brand-red);
    letter-spacing: -1px;
  }
  .email {
    top: 897px;
    font-family: "Montserrat", sans-serif;
    font-weight: 600;
    font-size: 38px;
    color: var(--brand-blue);
  }
  .services {
    top: 946px;
    font-family: "Oswald", sans-serif;
    font-weight: 500;
    font-size: 48px;
    color: var(--ink);
    display: flex;
    justify-content: center;
    align-items: center;
    gap: 12px;
    transform: scaleX(0.85);
    transform-origin: 600px 0;
  }
  .services .star { width: 24px; height: 24px; fill: var(--brand-red); }
</style>
</head>
<body>
  <div class="sticker"></div>
  <div class="truck-art" role="img" aria-label="Black outline illustration of a bucket truck with its boom raised"></div>

  <div class="line brand-name first">Brightline</div>
  <div class="line brand-name second">Upkeep</div>
  <div class="line brand-suffix">Incorporated</div>

  <div class="line service-call">FOR SERVICE CALL</div>
  <div class="line phone">877.555.0142</div>
  <div class="line email">Service@BrightlineUpkeep.com</div>
  <div class="line services">
    <span>ELECTRICAL</span>
    <svg class="star" viewBox="0 0 24 24" aria-hidden="true"><polygon points="12,1 15,9 23,9 16.5,14 19,22 12,17 5,22 7.5,14 1,9 9,9"/></svg>
    <span>LIGHTING</span>
    <svg class="star" viewBox="0 0 24 24" aria-hidden="true"><polygon points="12,1 15,9 23,9 16.5,14 19,22 12,17 5,22 7.5,14 1,9 9,9"/></svg>
    <span>SIGN SERVICE</span>
  </div>
</body>
</html>
```